Unique Realtor Website for real state Broker

All Real Estate websites look the same with the same boring layout and info that no one cares about. What I am looking for is a Realtor/Broker site but more focused on me and my services along with client reviews and testimonials. I am primarily a buyers Broker and a Military Specialist (KT) and that's what I want to focus on. I need a tab where I can put my listings, but I don't want listings to be the focus like most sites are. I also run a nonprofit dog rescue and I want a tab to talk about that as well. I am also looking to have a more mid-century feel to my site as mid-century architecture is my passion. I sell in both San Diego and Palm Springs. There's an artist based out of Palm Springs whom I love and I would like the feel of my site to have a similar vibe (attached are some of Pelts pieces to give you a better idea). I'm also having a cartoon drawing done of myself that I would like on the site as well (should be ready in a couple days). Want to make sure that the site is SEO focused as well. my current site is: www.torvekhomes.example for reference.

Target Market(s)

Buyers

Industry/Entity Type

Real Estate Agent

Coding

Coded - Design and coding required

Number of Pages Required

5+ page

Font styles to use
Sans Serif

Colors
fece3e
fee18a
ffffff
000000
959595

Requirements
Must have
• Must be unique, fun, buyer focused with SEO capability and strong social media base
• web site need to be designed for Word Press

```html
<!DOCTYPE html>
<html lang="en">
<head>
<meta charset="utf-8">
<title>Torvek Real Estate</title>
<link href="https://fonts.googleapis.com/css2?family=Nunito:wght@300;400;600;700&display=swap" rel="stylesheet">
<style>
:root{
  --yellow:#f6bd1e;
  --yellow-soft:#fee18a;
  --white:#ffffff;
  --ink:#222222;
  --text:#555555;
  --muted:#959595;
  --light:#f2f2f2;
  --footer:#333333;
  --footer-deep:#1b1b1b;
}
*{box-sizing:border-box;margin:0;padding:0}
html,body{width:1200px;height:3226px;overflow:hidden}
body{font-family:'Nunito',sans-serif;color:var(--text);background:var(--white);position:relative}
section,header,footer{position:absolute;left:0;width:1200px}
h2{font-weight:400;color:var(--ink);font-size:25px;letter-spacing:.5px}
p{font-size:13px;line-height:24px}
.btn{display:inline-block;background:var(--yellow);color:var(--white);font-size:12px;border-radius:20px;padding:9px 22px;text-transform:uppercase}
.photo{position:absolute}

.topbar{position:absolute;left:0;width:1200px;top:0;height:43px;background:var(--yellow);color:var(--white);font-size:12px}
.topbar .contact{position:absolute;left:90px;top:12px;display:flex;gap:24px;align-items:center}
.topbar .contact span{display:flex;gap:6px;align-items:center}
.topbar .social{position:absolute;right:90px;top:12px;display:flex;gap:8px}
.topbar .social i{width:16px;height:16px;background:rgba(255,255,255,.75);border-radius:2px;display:block}

.site-header{top:43px;height:97px;background:var(--white);box-shadow:0 2px 6px rgba(0,0,0,.12);z-index:2}
.brand{position:absolute;left:92px;top:22px;font-size:34px;font-weight:600;color:var(--yellow);letter-spacing:3px;line-height:40px}
.nav{position:absolute;right:90px;top:38px;display:flex;gap:40px;font-size:16px;color:var(--ink)}
.nav .active{color:var(--yellow)}

.hero{top:140px;height:550px;background:linear-gradient(180deg,#7fb6e6 0%,#b9d7ef 35%,#c9a57f 55%,#5f8f3c 78%,#4d7a2f 100%)}
.hero-title{position:absolute;left:88px;top:420px;color:var(--white);text-shadow:0 2px 4px rgba(0,0,0,.4)}
.hero-title h1{font-size:40px;font-weight:600;letter-spacing:.5px}
.hero-title div{font-size:27px;letter-spacing:.5px}
.slider-arrows{position:absolute;left:1052px;top:468px;display:flex;gap:6px}
.slider-arrows span{width:26px;height:26px;border-radius:50%;background:rgba(60,60,60,.7);display:flex;align-items:center;justify-content:center}

.welcome{top:690px;height:402px}
.welcome h2{position:absolute;left:90px;top:82px;font-size:27px}
.welcome p{position:absolute;left:90px;top:128px;width:525px;font-size:12px;line-height:25px}
.welcome .btn{position:absolute;left:90px;top:282px}
.welcome .frame{position:absolute;left:640px;top:58px;width:472px;height:278px;border:1px solid #ddd;padding:6px;background:var(--white);box-shadow:0 1px 4px rgba(0,0,0,.1)}
.welcome .frame .photo{inset:6px;background:linear-gradient(180deg,#5aa3d8 0%,#cfe2ee 45%,#e0d9c8 60%,#6f9a4e 100%)}

.services{top:1092px;height:388px;background:var(--light)}
.services h2{position:absolute;top:62px;width:1200px;text-align:center}
.service{position:absolute;top:112px;width:220px;text-align:center}
.service .ring{width:108px;height:108px;margin:0 auto;border-radius:50%;background:var(--white);border:1px solid #e2e2e2;display:flex;align-items:center;justify-content:center;box-shadow:0 0 0 6px rgba(255,255,255,.6)}
.service h3{font-weight:400;font-size:15px;color:var(--ink);margin-top:20px}
.service p{font-size:11px;line-height:18px;margin-top:8px;color:var(--text)}

.works{top:1480px;height:498px}
.works h2{position:absolute;top:70px;width:1200px;text-align:center}
.work{position:absolute;top:128px;width:330px}
.work .thumb{height:209px;border:1px solid #ddd;padding:4px;background:var(--white);position:relative}
.work .thumb .photo{inset:4px}
.work h3{font-weight:400;font-size:15px;color:var(--ink);margin-top:18px}
.work p{font-size:11px;line-height:20px;margin-top:6px;height:40px;overflow:hidden}
.work .more{font-size:11px;color:var(--yellow)}

.news{top:1978px;height:409px;background:var(--light)}
.news h2{font-size:19px}
.blog-title{position:absolute;left:90px;top:64px}
.post{position:absolute;left:90px;width:600px;height:116px}
.post .thumb{position:absolute;left:0;top:0;width:181px;height:116px;border:1px solid #ddd;background:var(--white)}
.post .thumb .photo{inset:4px}
.post .body{position:absolute;left:208px;top:4px}
.post h4{font-weight:400;font-size:13px;color:var(--ink)}
.post .date{font-size:10px;color:var(--ink);margin-top:8px}
.post p{font-size:12px;line-height:17px;margin-top:4px;color:var(--ink)}
.post .more{font-size:10px;color:var(--yellow)}
.reviews-title{position:absolute;left:772px;top:64px}
.quote{position:absolute;left:775px;top:100px;width:335px;height:154px;background:var(--yellow);color:var(--white);padding:20px 20px;font-size:11px;line-height:22px}
.quote:after{content:"";position:absolute;left:40px;bottom:-10px;border:10px solid transparent;border-bottom:0;border-top-color:var(--yellow)}
.reviewer{position:absolute;left:796px;top:272px;display:flex;align-items:center;gap:18px}
.reviewer .avatar{width:80px;height:80px;border-radius:50%;background:radial-gradient(circle,#c9a58b 0%,#8d7462 100%)}
.reviewer span{font-size:15px;color:var(--ink)}
.review-nav{position:absolute;left:896px;top:324px;display:flex;gap:4px}
.review-nav span{width:22px;height:22px;background:var(--white);border:1px solid #ddd;display:flex;align-items:center;justify-content:center}

.rescue{top:2387px;height:387px}
.rescue .frame{position:absolute;left:90px;top:53px;width:472px;height:273px;border:1px solid #ddd;padding:6px;background:var(--white)}
.rescue .frame .photo{inset:6px;background:linear-gradient(180deg,#8fb4c9 0%,#9a8d72 50%,#6b4e3a 100%)}
.rescue h2{position:absolute;left:592px;top:62px;font-size:24px}
.rescue h3{position:absolute;left:592px;top:100px;font-weight:400;font-size:15px;color:var(--muted)}
.rescue p{position:absolute;left:592px;top:124px;width:520px;font-size:12px;line-height:24px;text-align:justify}
.rescue .btn{position:absolute;left:592px;top:290px}

.partners{top:2774px;height:133px;display:flex;align-items:center;justify-content:space-between;padding:0 90px 0 128px}
.partners i{display:block;background:#b9b9b9;height:34px}

.site-footer{top:2907px;height:236px;background:var(--footer);color:var(--white)}
.site-footer h5{font-weight:400;font-size:16px;letter-spacing:.3px}
.col{position:absolute;top:46px}
.col p{font-size:11px;line-height:17px}
.signup input{display:block;margin-top:14px;width:214px;height:30px;border:0;background:#eee;padding:0 10px;font-family:inherit;font-size:10px}
.signup .btn{border-radius:0;padding:7px 16px;margin-top:14px;font-size:11px}
.tweet{display:flex;gap:8px;margin-top:18px;font-size:11px;line-height:17px}
.tweet em{color:#ddd}
.follow div{display:flex;align-items:center;gap:12px;margin-top:14px;font-size:11px}
.follow i{width:30px;height:30px;border-radius:50%;border:1px solid #888;display:block}
.copyright{position:absolute;left:0;width:1200px;top:3143px;height:83px;background:var(--footer-deep);color:var(--white);font-size:11px;text-align:center;line-height:83px}
</style>
</head>
<body>

<div class="topbar">
  <div class="contact">
    <span><svg width="11" height="11" viewBox="0 0 24 24"><path fill="#fff" d="M6.6 10.8a15 15 0 0 0 6.6 6.6l2.2-2.2c.3-.3.7-.4 1-.2 1.1.4 2.3.6 3.6.6.6 0 1 .4 1 1V20c0 .6-.4 1-1 1A17 17 0 0 1 3 4c0-.6.4-1 1-1h3.5c.6 0 1 .4 1 1 0 1.3.2 2.5.6 3.6.1.3 0 .7-.2 1z"/></svg>555-014-2290</span>
    <span><svg width="12" height="10" viewBox="0 0 24 18"><rect x="1" y="1" width="22" height="16" fill="none" stroke="#fff" stroke-width="2"/><path d="M1 1l11 9 11-9" fill="none" stroke="#fff" stroke-width="2"/></svg>hello@torvekhomes.example</span>
  </div>
  <div class="social"><i></i><i></i><i></i><i></i><i></i></div>
</div>

<header class="site-header">
  <div class="brand">TORVEK</div>
  <nav class="nav">
    <span class="active">HOME</span><span>ABOUT</span><span>SERVICES</span><span>LISTING</span><span>REVIEWS</span><span>BLOG</span><span>CONTACT</span><span>RESCUE</span>
  </nav>
</header>

<section class="hero">
  <div class="photo" style="inset:0" role="img" aria-label="Photo of a two-storey stucco family home with a green lawn under a blue sky"></div>
  <div class="hero-title">
    <h1>REAL ESTATE BROKER</h1>
    <div>NEQUE PORRO QUISQUAM EST QUI</div>
  </div>
  <div class="slider-arrows">
    <span><svg width="10" height="10" viewBox="0 0 10 10"><path d="M7 1L3 5l4 4" stroke="#fff" stroke-width="1.6" fill="none"/></svg></span>
    <span><svg width="10" height="10" viewBox="0 0 10 10"><path d="M3 1l4 4-4 4" stroke="#fff" stroke-width="1.6" fill="none"/></svg></span>
  </div>
</section>

<section class="welcome">
  <h2>WELCOME TO TORVEK REAL ESTATE</h2>
  <p>I am proud to say that I have helped countless Military families find their perfect homes and I am constantly striving to improve my service to them. Thats why I decided to get my Service Family Relocation Specialist (SFRS) certification. According to the official SFRS website, www.relocationpro.example, Agents with the SFRS certification,&amp; When military staff and their families relocate, the services of a real estate professional who understands their needs and timetables makes the transfer easier, faster, and less stressful.</p>
  <span class="btn">Read More</span>
  <div class="frame"><div class="photo" role="img" aria-label="Photo of a mid-century modern house with a stone wall, yellow door and palm trees"></div></div>
</section>

<section class="services">
  <h2>OUR SERVICES</h2>
  <div class="service" style="left:86px">
    <div class="ring"><svg width="30" height="34" viewBox="0 0 30 34"><rect x="6" y="2" width="18" height="30" fill="var(--yellow)"/><g fill="#fff"><rect x="10" y="7" width="3" height="3"/><rect x="17" y="7" width="3" height="3"/><rect x="10" y="13" width="3" height="3"/><rect x="17" y="13" width="3" height="3"/><rect x="10" y="19" width="3" height="3"/><rect x="17" y="19" width="3" height="3"/><rect x="13" y="25" width="4" height="7"/></g></svg></div>
    <h3>NEQUE QUISQUAM</h3>
    <p>Born to a Top-producing Agent mother (or Ma as I like to call her) and a Real Estate developer father, Real Estate</p>
  </div>
  <div class="service" style="left:354px">
    <div class="ring"><svg width="32" height="32" viewBox="0 0 24 24"><path fill="var(--yellow)" d="M22.7 19l-9.1-9.1c.9-2.3.4-5-1.5-6.9-2-2-5-2.4-7.4-1.3L9 6 6 9 1.6 4.7C.4 7.1.9 10.1 2.9 12.1c1.9 1.9 4.6 2.4 6.9 1.5l9.1 9.1c.4.4 1 .4 1.4 0l2.3-2.3c.5-.4.5-1.1.1-1.4z"/></svg></div>
    <h3>PORRO QUISQUAM</h3>
    <p>Born to a Top-producing Agent mother (or Ma as I like to call her) and a Real Estate developer father, Real Estate</p>
  </div>
  <div class="service" style="left:622px">
    <div class="ring"><svg width="34" height="30" viewBox="0 0 34 30"><path fill="var(--yellow)" d="M17 2L2 15h4v13h8v-8h6v8h8V15h4z"/></svg></div>
    <h3>QUISQUAM EST</h3>
    <p>Born to a Top-producing Agent mother (or Ma as I like to call her) and a Real Estate developer father, Real Estate</p>
  </div>
  <div class="service" style="left:890px">
    <div class="ring"><svg width="36" height="26" viewBox="0 0 36 26"><rect x="6" y="2" width="24" height="16" fill="none" stroke="var(--yellow)" stroke-width="2.5"/><path d="M2 21h32l-2 3H4z" fill="var(--yellow)"/></svg></div>
    <h3>DOLOREM IPSUM</h3>
    <p>Born to a Top-producing Agent mother (or Ma as I like to call her) and a Real Estate developer father, Real Estate</p>
  </div>
</section>

<section class="works">
  <h2>OUR WORKS</h2>
  <div class="work" style="left:90px">
    <div class="thumb"><div class="photo" style="background:linear-gradient(180deg,#3fb0c9 0%,#f2b13a 55%,#2e8fb5 100%)" role="img" aria-label="Colourful mid-century pool party illustration"></div></div>
    <h3>NEQUE PORRO QUISQUAM</h3>
    <p>Another big passion of mine is mid-century architecture. I absolutely love the style of homes from this era and every-</p>
    <span class="more">Learn More →</span>
  </div>
  <div class="work" style="left:441px">
    <div class="thumb"><div class="photo" style="background:linear-gradient(180deg,#3a3f9a 0%,#7a4fb0 50%,#d9679a 100%)" role="img" aria-label="Colourful illustration of costumed party guests"></div></div>
    <h3>NEQUE PORRO QUISQUAM</h3>
    <p>Another big passion of mine is mid-century architecture. I absolutely love the style of homes from this era and every-</p>
    <span class="more">Learn More →</span>
  </div>
  <div class="work" style="left:789px">
    <div class="thumb"><div class="photo" style="background:linear-gradient(180deg,#e8893a 0%,#e9b15a 50%,#b7824c 100%)" role="img" aria-label="Warm desert illustration of a mid-century house with palm trees and dog walkers"></div></div>
    <h3>NEQUE PORRO QUISQUAM</h3>
    <p>Another big passion of mine is mid-century architecture. I absolutely love the style of homes from this era and every-</p>
    <span class="more">Learn More →</span>
  </div>
</section>

<section class="news">
  <h2 class="blog-title">LATEST BLOG</h2>
  <div class="post" style="top:100px">
    <div class="thumb"><div class="photo" style="background:linear-gradient(180deg,#9cc7e6 0%,#d8c7a8 55%,#7a6a55 100%)" role="img" aria-label="Photo of a patio dining set beside a pool"></div></div>
    <div class="body">
      <h4>Nemo Enim Ipsam Voluptatem</h4>
      <div class="date">JULY 20, 2017</div>
      <p>Lorem ipsum dolor sit amet, consectetur adipiscing elit, sed do<br>eiusmod tempor incididunt ut labore</p>
      <span class="more">Read more »</span>
    </div>
  </div>
  <div class="post" style="top:241px">
    <div class="thumb"><div class="photo" style="background:linear-gradient(180deg,#c98a52 0%,#8a4d2a 60%,#5c3320 100%)" role="img" aria-label="Photo of a wooden dining room table with chairs"></div></div>
    <div class="body">
      <h4>Nemo Enim Ipsam Voluptatem</h4>
      <div class="date">JULY 20, 2017</div>
      <p>Lorem ipsum dolor sit amet, consectetur adipiscing elit, sed do<br>eiusmod tempor incididunt ut labore</p>
      <span class="more">Read more »</span>
    </div>
  </div>
  <h2 class="reviews-title">REVIEWS</h2>
  <div class="quote">❝ Lorem Ipsum has been the industry's standard dummy text ever since the 1500s, when an unknown printer took a galley of type and scrambled it to make a type specimen book. It has survived only five ❞</div>
  <div class="reviewer">
    <div class="avatar" role="img" aria-label="Portrait photo of the reviewer"></div>
    <span>John Doe - Manager</span>
  </div>
  <div class="review-nav">
    <span><svg width="8" height="8" viewBox="0 0 10 10"><path d="M7 1L3 5l4 4" stroke="#555" stroke-width="1.6" fill="none"/></svg></span>
    <span><svg width="8" height="8" viewBox="0 0 10 10"><path d="M3 1l4 4-4 4" stroke="#555" stroke-width="1.6" fill="none"/></svg></span>
  </div>
</section>

<section class="rescue">
  <div class="frame"><div class="photo" role="img" aria-label="Photo of the rescue co-founders sitting on a deck with their dogs"></div></div>
  <h2>RESCUE</h2>
  <h3>Co-Founder of The Canine Harbor</h3>
  <p>Since childhood, my number one passion has been animal advocacy (In case you were wondering, yes, I was that girl who protested the frog dissection in Biology class). When I co-founded The Canine Harbor in 2010, my dream of saving dogs in need was finally realized. We have saved hundreds of dogs and we focus on rescuing from high kill shelters in Southern California and from the streets of Mexico. We are a 501c Non Profit organization and we are 100% donation and volunteer run. If you are interested in learning more,</p>
  <span class="btn">Read More</span>
</section>

<section class="partners" aria-label="Partner badges">
  <i style="width:250px;height:40px"></i>
  <i style="width:110px;height:28px"></i>
  <i style="width:120px;height:30px"></i>
  <i style="width:84px;height:36px"></i>
  <i style="width:118px;height:34px"></i>
</section>

<footer class="site-footer">
  <div class="col signup" style="left:100px;width:240px">
    <h5>NEWSLETTERS SIGN UP</h5>
    <p style="margin-top:10px">Sign up for our daily email by entering your information below</p>
    <input type="text" placeholder="Email address">
    <span class="btn">Subscribe</span>
  </div>
  <div class="col" style="left:398px;width:240px">
    <h5>LATEST POSTS</h5>
    <div class="tweet"><svg width="14" height="12" viewBox="0 0 14 12"><circle cx="7" cy="6" r="5" fill="#fff"/></svg><div>Featured Workspace : Studio Nine link.example/9Qx2 <em>10 hours ago</em></div></div>
    <div class="tweet"><svg width="14" height="12" viewBox="0 0 14 12"><circle cx="7" cy="6" r="5" fill="#fff"/></svg><div>Featured Workspace : Studio Nine link.example/9Qx2 <em>10 hours ago</em></div></div>
  </div>
  <div class="col" style="left:700px;width:220px">
    <h5>GET IN TOUCH</h5>
    <p style="margin-top:14px;line-height:28px">Address : 480 Harbor Lane<br>San Diego, Ca 92101<br>Phone : 555-014-2290<br>Email : hello@torvekhomes.example</p>
  </div>
  <div class="col follow" style="left:974px;width:150px">
    <h5>FOLLOW US ON</h5>
    <div><i></i>Linkwave</div>
    <div><i></i>Postline</div>
    <div><i></i>Snapgrid</div>
  </div>
</footer>

<div class="copyright">Copyright © 2017. All Rights Reserved</div>

</body>
</html>
```